Website for Franchise Builder

We are a web design and Architectural company that is selling an all in one Business solution for small to medium size builders.

We are Frame KV..

We are providing builders with the following services:

1. Dynamic Site quarry websites and Zentap Apps
2. Rebranded housed plans with Brochures
3. Logo and Corporate identity
4. Estimating software
5. 3d Visualisation and Rendering
5. Building design and Planning support.

We will be helping builders to complete and have a competitive edge against the large franchise building companies. Who control the House building market in Australia. The large companies have great website, apps, brochures and standard house plans. So that is exactly what we will be providing our builders. At a fraction of the normal cost. We will have help them to win jobs and look more professional.

My current website is:

http://norvellpage.sitequarry.com

I have attached and provided the following:

1. whole website Mock-up
2. Separated competition Pages to mock-up
2. Logo (in latest advertisement zip file)
4. Images and that my be useful
5. Some information on our services
6. Latest magazine advertisement (notice the ad also displays the roofdraftguild. Which is a separate website that sells our house plans)

The five pages i would like designed for the competition are follows:

1. Home Page
2. What we do - Websites & Zentap Apps
3. How it works
4. Our work - Display individual websites similar to the way www.plomarex.com displays their websites
5. Builders packages (pricing table. Mockup has incorrect items for table. See please pdf with correct data for table)

Please use the mock-ups as a guide only. Go for it with your creativity please.

Sites that i really like are:

- www.plomarex.com
- www.quillmarket.com.au

Target Market(s)

Builders and Wifes of Builders

Industry/Entity Type

Business

Requirements
Must have
• 1. Testimonails displayed on home page somewhere
2. Social media on home page, and on individual pages displaying websites

Nice to have
• I really like the www.plomarex.com. The way they use icons and have the catch phrases. We could have catch phase such as:

1. All in one Business Solution for builders
2. Lets Get Started View websites
3. Ready to Go Business Solutions for Builders.

```html
<!DOCTYPE html>
<html lang="en">
<head>
<meta charset="utf-8">
<title>Frame KV – Builders IT Solutions</title>
<link rel="stylesheet" href="https://fonts.googleapis.com/css2?family=Arimo:wght@400;700&family=Open+Sans:wght@400;700&family=Gelasio:ital@1&display=swap">
<style>
:root{
  --blue:#1470c0;
  --blue-dark:#0d5aa0;
  --ink:#222;
  --text:#555;
  --muted:#888;
  --line:#d6d6d6;
  --rule:#3d7fb3;
  --panel:#f4f4f4;
  --white:#fff;
}
*{margin:0;padding:0;box-sizing:border-box}
html,body{width:834px;height:1200px;overflow:hidden;background:var(--white)}
body{position:relative;font-family:Arimo,Arial,sans-serif;color:var(--ink)}
.abs{position:absolute}

/* header */
.brand{left:83px;top:52px;display:flex;align-items:center;gap:8px;font-size:22px;font-weight:400;color:var(--ink)}
.brand-mark{width:12px;height:12px;background:var(--ink)}
.social{right:84px;top:14px;display:flex;gap:8px}
.social span{width:19px;height:19px;border-radius:4px;background:var(--blue)}
.call{right:83px;top:48px;display:flex;align-items:center;gap:7px;font-weight:700}
.call .label{font-size:12.5px;color:var(--ink)}
.call .num{font-size:16px}
.toplinks{left:407px;top:87px;display:flex;font-size:9.5px}
.toplinks a{color:var(--ink);text-decoration:none;padding:0 8px;border-right:1px solid var(--ink);line-height:12px}
.toplinks a:last-child{border:0}
.search{left:619px;top:80px;width:131px;height:26px;border:1px solid var(--line);border-radius:3px;font-size:9px;color:var(--text);padding:8px 10px}
.search svg{position:absolute;right:7px;top:7px}

.mainnav{left:0;top:121px;width:834px;height:34px;border-top:1px solid var(--rule);border-bottom:1px solid var(--rule);display:flex;align-items:center;padding-left:88px;gap:30px;font-size:10.5px}
.mainnav a{color:var(--ink);text-decoration:none}

/* hero */
.hero-title{left:96px;top:236px;font-size:18px;font-weight:700;color:#3a3a3a;line-height:22px}
.hero-copy{left:96px;top:285px;width:180px;font-size:8px;color:var(--text);line-height:11px}
.btn{background:var(--blue);color:var(--white);font-weight:700;border-radius:3px;text-align:center}
.hero-btn{left:95px;top:333px;width:76px;height:23px;font-size:9.5px;line-height:23px}
.shot-back{left:308px;top:236px;width:102px;height:184px;background:linear-gradient(#eaeaea,#cfcfcf);border:1px solid #ccc}
.shot-front{left:407px;top:207px;width:339px;height:213px;background:linear-gradient(180deg,#ececec 0 10%,#dfe6ee 10% 20%,#5a6b80 20% 72%,#2b3440 72%);border:1px solid #bbb;box-shadow:0 2px 6px rgba(0,0,0,.2)}
.hero-base{left:0;top:419px;width:834px;height:1px;background:var(--line)}

/* intro */
.intro{left:90px;top:448px;width:656px;font-family:Gelasio,Georgia,serif;font-style:italic;font-size:11.5px;line-height:18px;color:#333}
.intro em{color:var(--blue);font-size:12.5px}
.intro-rule{left:64px;top:509px;width:706px;height:1px;background:linear-gradient(90deg,transparent,#ddd,transparent)}

/* testimonials */
.testimonials{left:84px;top:547px;width:204px;height:285px;border:1px solid #ccc;background:var(--panel);border-radius:2px;box-shadow:0 1px 3px rgba(0,0,0,.12)}
.testimonials h3{font-family:"Open Sans",sans-serif;font-size:11px;font-weight:700;color:#444;padding:11px 9px;height:31px;border-bottom:1px solid #ddd;background:linear-gradient(#f8f8f8,#e9e9e9)}
.tools{position:absolute;right:7px;top:7px;display:flex;gap:2px}
.tools span{width:15px;height:15px;border:1px solid #bbb;background:#fafafa;font-size:11px;line-height:13px;text-align:center;color:#444}
.quote{padding:12px 9px 8px;font-family:"Open Sans",sans-serif}
.quote + .quote{border-top:1px solid #e6e6e6;background:#f0f0f0}
.who{display:flex;gap:10px;margin-bottom:10px}
.avatar{width:36px;height:36px;background:linear-gradient(#c8ccd2,#6d737c);border:1px solid #ccc}
.who b{display:block;font-size:8px;margin-top:2px}
.who small{display:block;font-size:7px;color:#333;margin-top:4px}
.who i{display:block;font-family:Gelasio,serif;font-size:7px;color:var(--muted);margin-top:3px}
.quote p{font-family:Gelasio,Georgia,serif;font-style:italic;font-size:7.5px;line-height:12.5px;color:#333}

.video{left:83px;top:859px;width:206px;height:185px;border:1px solid #ddd;border-radius:6px;box-shadow:0 1px 3px rgba(0,0,0,.12)}
.video-frame{position:absolute;left:7px;top:6px;width:192px;height:145px;background:linear-gradient(#1c2733,#55677a 60%,#2a3038)}
.video-bar{position:absolute;left:0;bottom:0;width:100%;height:11px;background:#111}
.video-bar i{position:absolute;left:34px;top:5px;width:120px;height:2px;background:#555}
.video-bar i::before{content:"";position:absolute;left:0;top:0;width:50px;height:2px;background:#eee}
.video p{position:absolute;left:0;top:160px;width:100%;text-align:center;font-size:11px;font-weight:700}

/* services */
.service{width:176px}
.service h4{font-size:12.5px;font-weight:700;line-height:17px;color:var(--ink)}
.service .body{margin-top:10px;font-size:8px;line-height:11.8px;color:var(--text)}
.service svg{float:left;margin:0 8px 4px 0}

/* cta */
.cta-rule{left:0;top:1081px;width:834px;height:2px;background:#ddd}
.cta-text{left:82px;top:1106px;font-size:15.5px;color:#333}
.cta-btn{left:645px;top:1102px;width:106px;height:27px;font-size:12.5px;line-height:27px;border-radius:14px;border:2px solid var(--blue-dark)}

/* footer */
.footer{left:0;top:1146px;width:834px;height:54px;border-top:1px solid #ddd;background:#fafafa}
.foot-brand{left:84px;top:1165px;display:flex;align-items:center;gap:5px;font-size:12px;font-weight:400;color:#777}
.foot-brand span{width:6px;height:6px;background:#999}
.copy{left:160px;top:1168px;font-size:8.5px;color:#333}
.legal{right:84px;top:1168px;font-size:8.5px;color:#333}
</style>
</head>
<body>

<header>
  <div class="abs brand"><span class="brand-mark"></span>Frame KV</div>
  <div class="abs social" aria-label="Social media"><span></span><span></span><span></span></div>
  <div class="abs call">
    <span class="label">CALL US</span>
    <svg width="20" height="20" viewBox="0 0 20 20"><circle cx="10" cy="10" r="10" fill="var(--blue)"/><path d="M7 5c1 0 2 2 2 3s-1 1-1 2 2 3 3 3 1-1 2-1 3 1 3 2-2 2-3 2C9 16 4 11 4 8c0-1 2-3 3-3z" fill="#fff"/></svg>
    <span class="num">1300 555 014</span>
  </div>
  <nav class="abs toplinks"><a>Support</a><a>Client Portal</a><a>Contact</a><a>About</a></nav>
  <div class="abs search">Search
    <svg width="10" height="10" viewBox="0 0 10 10"><circle cx="4" cy="4" r="3" fill="none" stroke="var(--blue)" stroke-width="1.5"/><path d="M6 6l3 3" stroke="var(--blue)" stroke-width="1.6"/></svg>
  </div>
  <nav class="abs mainnav">
    <a>What we do</a><a>Builder Packages</a><a>How it works</a><a>Site quarry</a><a>Support Network</a><a>Our Work</a><a>Free trial</a>
  </nav>
</header>

<section class="hero">
  <h1 class="abs hero-title">All in one Business<br>Solutions for Builders</h1>
  <p class="abs hero-copy">Lorem ipsum dolor sit amet consectetuer adipiscing elit nunc ullamcorper blandit urna. venenatis libero.</p>
  <div class="abs btn hero-btn">Learn More</div>
  <div class="abs shot-back" role="img" aria-label="Screenshot of a builder website shown in a browser window"></div>
  <div class="abs shot-front" role="img" aria-label="Screenshot of a client business website with office photo banner shown in a browser window"></div>
  <div class="abs hero-base"></div>
</section>

<p class="abs intro"><em>What we do?</em> Nunc luctus porta mi a estib ulum Etiam sem nisl auctor sit amet molestie sed pharetra a purus. Fusce massa dolor, facilisis eu sagittis elementum, porttitor id nisi. Dus vel ipsum neque.</p>
<div class="abs intro-rule"></div>

<aside class="abs testimonials">
  <h3>TESTIMONIALS</h3>
  <div class="tools"><span>&#8964;</span><span>+</span><span>&times;</span></div>
  <div class="quote">
    <div class="who"><div class="avatar" role="img" aria-label="Portrait of Marcus Hale"></div><div><b>Marcus Hale</b><small>Managing Director Orchardline UK</small><i>Orchardline.co.uk</i></div></div>
    <p>“Donec sed odio dui. Nulla vitae elit libero, a pharetra augue. Nullam id dolor id nibh ultricies vehicula ut id elit. Integer posuere erat a ante venenatis dapibus posuere velit aliquet...”</p>
  </div>
  <div class="quote">
    <div class="who"><div class="avatar" role="img" aria-label="Portrait of Peter Lowry"></div><div><b>Peter Lowry</b><small>Technical Director Voltera International</small><i>Voltera.com</i></div></div>
    <p>“Donec sed odio dui. Nulla vitae elit libero, a pharetra augue. Nullam id dolor id nibh ultricies vehicula ut id elit. Integer posuere erat a ante venenatis dapibus posuere velit aliquet...”</p>
  </div>
</aside>

<div class="abs video">
  <div class="video-frame" role="img" aria-label="Video still of a modern multi-storey building at dusk"><div class="video-bar"><i></i></div></div>
  <p>Watch this video on your website</p>
</div>

<section class="services">
  <div class="abs service" style="left:340px;top:546px">
    <h4>Online Marketing &amp; Social Media</h4>
    <div class="body"><svg width="28" height="28" viewBox="0 0 28 28"><circle cx="14" cy="14" r="13" fill="var(--blue)"/><path d="M6 8c4 0 5 3 3 5s1 5-1 8M18 4c-2 3 1 5 4 5M16 16c3-1 6 1 5 5" stroke="#fff" stroke-width="2" fill="none"/></svg>Integer egestas ultricies urna vitae molestie. Donec nec facilisis nisi. Vivamus tempor feugiat velit gravida vehicula. Donec faucibus pellentesque ipsum id varius. Ut rutrum metus sed neque ultricies a dictum ante sagittis.</div>
  </div>
  <div class="abs service" style="left:575px;top:546px">
    <h4>Completely Rebrandable House Plans</h4>
    <div class="body"><svg width="30" height="26" viewBox="0 0 30 26"><path d="M15 1L1 13h4v12h7v-8h6v8h7V13h4z" fill="var(--blue)"/></svg>Integer egestas ultricies urna vitae molestie. Donec nec facilisis nisi. Vivamus tempor feugiat velit gravida vehicula. Donec faucibus pellentesque ipsum id varius. Ut rutrum metus sed neque ultricies a dictum ante sagittis.</div>
  </div>
  <div class="abs service" style="left:340px;top:684px">
    <h4>Construction Estimating Software</h4>
    <div class="body"><svg width="30" height="28" viewBox="0 0 30 28"><ellipse cx="14" cy="17" rx="11" ry="8" fill="var(--blue)"/><circle cx="14" cy="5" r="4" fill="var(--blue)"/><rect x="7" y="22" width="4" height="5" fill="var(--blue)"/><rect x="17" y="22" width="4" height="5" fill="var(--blue)"/><path d="M25 14c2 0 3-1 3-3" stroke="var(--blue)" stroke-width="1.5" fill="none"/></svg>Integer egestas ultricies urna vitae molestie. Donec nec facilisis nisi. Vivamus tempor feugiat velit gravida vehicula. Donec faucibus pellentesque ipsum id varius. Ut rutrum metus sed neque ultricies a dictum ante sagittis.</div>
  </div>
  <div class="abs service" style="left:575px;top:684px">
    <h4>Awesome Support<br>24/7</h4>
    <div class="body"><svg width="28" height="28" viewBox="0 0 20 20"><circle cx="10" cy="10" r="10" fill="var(--blue)"/><path d="M7 5c1 0 2 2 2 3s-1 1-1 2 2 3 3 3 1-1 2-1 3 1 3 2-2 2-3 2C9 16 4 11 4 8c0-1 2-3 3-3z" fill="#fff"/></svg>Integer egestas ultricies urna vitae molestie. Donec nec facilisis nisi. Vivamus tempor feugiat velit gravida vehicula. Donec faucibus pellentesque ipsum id varius. Ut rutrum metus sed neque ultricies a dictum ante sagittis.</div>
  </div>
  <div class="abs service" style="left:340px;top:822px">
    <h4>Websites &amp; Zentap Apps</h4>
    <div class="body"><svg width="28" height="30" viewBox="0 0 28 30"><rect x="6" y="1" width="16" height="28" rx="3" fill="var(--blue)"/><rect x="8.5" y="5" width="11" height="18" fill="#fff"/><circle cx="14" cy="26" r="1.4" fill="#fff"/></svg>Integer egestas ultricies urna vitae molestie. Donec nec facilisis nisi. Vivamus tempor feugiat velit gravida vehicula. Donec faucibus pellentesque ipsum id varius. Ut rutrum metus sed neque ultricies a dictum ante sagittis.</div>
  </div>
  <div class="abs service" style="left:575px;top:822px">
    <h4>Branding &amp; Logos</h4>
    <div class="body"><svg width="28" height="28" viewBox="0 0 28 28"><path d="M14 1l3.8 8.4 9.2.9-6.9 6.1 2 9-8.1-4.7-8.1 4.7 2-9L1 10.3l9.2-.9z" fill="var(--blue)"/></svg>Integer egestas ultricies urna vitae molestie. Donec nec facilisis nisi. Vivamus tempor feugiat velit gravida vehicula. Donec faucibus pellentesque ipsum id varius. Ut rutrum metus sed neque ultricies a dictum ante sagittis.</div>
  </div>
  <div class="abs service" style="left:340px;top:946px">
    <h4>Planning and Building Design</h4>
    <div class="body"><svg width="30" height="28" viewBox="0 0 30 28"><circle cx="11" cy="11" r="7" fill="none" stroke="var(--blue)" stroke-width="4" stroke-dasharray="3 2"/><circle cx="11" cy="11" r="3" fill="var(--blue)"/><circle cx="23" cy="20" r="5" fill="none" stroke="var(--blue)" stroke-width="3" stroke-dasharray="2 1.6"/></svg>Integer egestas ultricies urna vitae molestie. Donec nec facilisis nisi. Vivamus tempor feugiat velit gravida vehicula. Donec faucibus pellentesque ipsum id varius. Ut rutrum metus sed neque ultricies a dictum ante sagittis.</div>
  </div>
  <div class="abs service" style="left:575px;top:946px">
    <h4>3d Visualisation &amp; Rendering</h4>
    <div class="body"><svg width="30" height="28" viewBox="0 0 30 28"><rect x="1" y="2" width="28" height="19" rx="2" fill="var(--blue)"/><rect x="4" y="5" width="22" height="13" fill="#fff"/><rect x="11" y="21" width="8" height="4" fill="var(--blue)"/><rect x="7" y="25" width="16" height="2" fill="var(--blue)"/></svg>Integer egestas ultricies urna vitae molestie. Donec nec facilisis nisi. Vivamus tempor feugiat velit gravida vehicula. Donec faucibus pellentesque ipsum id varius. Ut rutrum metus sed neque ultricies a dictum ante sagittis.</div>
  </div>
</section>

<section class="cta">
  <div class="abs cta-rule"></div>
  <p class="abs cta-text">I’m interested in giving my business the competitive edge</p>
  <div class="abs btn cta-btn">Send Enquiry</div>
</section>

<footer>
  <div class="abs footer"></div>
  <div class="abs foot-brand"><span></span>Frame KV</div>
  <p class="abs copy">© Copyright 2012 Frame KV , All Rights Reserved</p>
  <p class="abs legal">Terms and Conditions &nbsp;|&nbsp; Sitemap &nbsp;|&nbsp; Privacy Policy</p>
</footer>

</body>
</html>
```